LABEL DESIGN FOR A NATURAL SKIN CARE LINE

We are looking for a label design for a new natural skin care line that targets the mindfulness and yoga community. We offer a everyday face wash that is derived from natural ingredients and combine it with online yoga classes that will match the intention on the back of the product label. Please make the logo prominent on the front of the bottle, play with horizontal and vertical placement. The product is called “Mellow Rinse”. We like a more modern clean feel.

DERMAVOW is essentially a natural wellness beauty brand that will fuse into a line of products, a design should be versatile and include the colors in the logo along with whites. The final design should communicate a natural feel that will speak to the yoga community and mindfulness movement.

Target Market(s)

Yogis, fitness community, natural products

Industry/Entity Type

Skin Care Product

Font styles to use
Serif
Decorative

Requirements
Must have
• logo on the front that is prominent, with “MELLOW RINSE” as the product name.

Bottle Dimensions:
3OZ 3.35x4.75in (check attachments)
Nice to have
• Unique designs that stand out. Use the colors in logo. Would be great to have a third eye as a watermark
Should not have
• dark colors,

```html
<!DOCTYPE html>
<html lang="en">
<head>
<meta charset="utf-8">
<title>DERMAVOW Mellow Rinse Label</title>
<link rel="stylesheet" href="https://fonts.googleapis.com/css2?family=Josefin+Sans:wght@400&display=swap">
<style>
  :root {
    --page: #f4f5f4;
    --label: #ffffff;
    --frame: #2b2b2b;
    --brand-green: #8cc63f;
    --brand-teal: #1fb3a0;
    --mark-fill: #eaf6f1;
    --lotus-deep: rgba(92, 186, 78, 0.8);
    --lotus-soft: rgba(140, 206, 120, 0.28);
    --lotus-clear: rgba(255, 255, 255, 0);
  }
  * { box-sizing: border-box; margin: 0; padding: 0; }
  html, body { width: 1200px; height: 1111px; overflow: hidden; }
  body {
    background: var(--page);
    font-family: "Josefin Sans", sans-serif;
    position: relative;
  }
  .label-panel {
    position: absolute;
    top: 357px;
    width: 564px;
    height: 396px;
    background: var(--label);
    border: 1.5px solid var(--frame);
    overflow: hidden;
  }
  .label-front { left: 30px; }
  .label-side { left: 604px; }

  .brand-mark {
    position: absolute;
    border-radius: 50%;
    background: var(--mark-fill);
    border: 3px solid var(--brand-green);
  }
  .brand-name {
    position: absolute;
    color: var(--brand-teal);
    font-weight: 400;
    letter-spacing: 1px;
    white-space: nowrap;
    line-height: 1;
  }
  .product-name {
    position: absolute;
    color: var(--brand-teal);
    font-weight: 400;
    letter-spacing: 4px;
    white-space: nowrap;
    line-height: 1;
  }

  .label-front .brand-mark { left: 230px; top: 36px; width: 104px; height: 104px; }
  .label-front .brand-name { left: 0; width: 100%; text-align: center; top: 148px; font-size: 32px; }
  .label-front .product-name { left: 0; width: 100%; text-align: center; top: 192px; font-size: 15px; }

  .label-side .brand-mark { left: 223px; top: 151px; width: 88px; height: 88px; }
  .label-side .brand-name {
    left: 328px; top: 195px; font-size: 26px;
    transform: translate(-50%, -50%) rotate(-90deg);
  }

  .lotus {
    position: absolute;
    background: radial-gradient(ellipse 50% 100% at 50% 100%, var(--lotus-deep) 0%, var(--lotus-soft) 55%, var(--lotus-clear) 100%);
  }
  .lotus-flipped {
    background: radial-gradient(ellipse 50% 100% at 50% 0%, var(--lotus-deep) 0%, var(--lotus-soft) 55%, var(--lotus-clear) 100%);
  }
  .label-front .lotus { left: 153px; top: 240px; width: 258px; height: 150px; }
  .label-side .lotus-top { left: 204px; top: 5px; width: 177px; height: 98px; }
  .label-side .lotus-bottom { left: 204px; top: 283px; width: 177px; height: 108px; }
</style>
</head>
<body>
  <section class="label-panel label-front">
    <div class="brand-mark"></div>
    <div class="brand-name">DERMAVOW</div>
    <div class="product-name">MELLOW RINSE</div>
    <div class="lotus" role="img" aria-label="Soft green translucent lotus flower illustration"></div>
  </section>
  <section class="label-panel label-side">
    <div class="lotus lotus-top" role="img" aria-label="Soft green translucent lotus flower illustration"></div>
    <div class="brand-mark"></div>
    <div class="brand-name">DERMAVOW</div>
    <div class="lotus lotus-flipped lotus-bottom" role="img" aria-label="Inverted soft green translucent lotus flower illustration"></div>
  </section>
</body>
</html>
```